Complete Blazewren rebranding web-design

Toss up an "under construction" page and deliver a new modern marketing website for a business to business Fire Protection Company.

Incorporating the best and most recent SEO techniques for local searches, targeted key word searches and messaging for the 5 major company services.

Total of about 10 pages.

Very simple commerce page for local delivery or customer pickup of 5 products (Fire Extinguishers).

Incorporating social media related (designed) ad templates and a blog / email news letter section.

Target Market(s)

Facilities Managers, maintenance managers, building manager, operations managers for any company in San Diego county and surrounding areas.

Industry/Entity Type

Fire Safety

Font styles to use
Serif
Sans Serif

Colors
ec1f27
f37122
f78f20
fec214
fbed22

Requirements
Must have
• Fast dynamic loading website optimized for mobile viewing and desktop.
• Full SEO key word driven pages for 5 services and no more then 10 pages total.

```html
<!DOCTYPE html>
<html lang="en">
<head>
<meta charset="utf-8">
<title>Blazewren Fire &amp; Safety</title>
<link href="https://fonts.googleapis.com/css2?family=Roboto:wght@300;400;500;700&display=swap" rel="stylesheet">
<style>
:root{
  --red:#ec1f27;
  --orange:#f37122;
  --amber:#f78f20;
  --gold:#fec214;
  --dark:#1f1f1f;
  --text:#333;
  --muted:#777;
  --line:#ddd;
  --band:#ebebeb;
}
*{margin:0;padding:0;box-sizing:border-box}
html,body{width:678px;height:1200px;overflow:hidden;background:#fff}
body{font-family:'Roboto',sans-serif;color:var(--text);position:relative}
.abs{position:absolute}
.topbar{left:0;top:0;width:678px;height:18px;background:#1a1a1a;color:#fff;font-size:7px;line-height:18px;padding-left:56px}
.topbar .phone{color:var(--orange)}
.quote-btn{right:79px;top:3px;height:12px;background:var(--red);color:#fff;font-size:5.5px;line-height:12px;padding:0 6px}
.header{left:0;top:18px;width:678px;height:52px;background:linear-gradient(#2b2b2b,#151515)}
.nav{top:18px;height:52px;line-height:52px;color:#ddd;font-size:7.5px;text-transform:uppercase}
.brand{left:288px;top:28px;width:100px;text-align:center;font-size:15px;font-weight:700;color:var(--amber)}
.brand-dot{display:inline-block;width:8px;height:8px;border-radius:50%;background:var(--red);margin-right:4px;vertical-align:middle}
.hero{left:0;top:70px;width:678px;height:272px;background:linear-gradient(90deg,#b5b4b1,#cfceca 50%,#bab9b5)}
.hero-photo{left:120px;top:70px;width:140px;height:272px;background:linear-gradient(90deg,#8e1010,#d42420 50%,#9a1414)}
.hero-title{left:315px;top:148px;color:#fff;font-size:21px;font-weight:500;line-height:25px;white-space:nowrap}
.hero-sub{left:318px;top:205px;color:#fff;font-size:11px;line-height:18px;width:260px}
.btn{background:var(--red);color:#fff;font-size:7.5px;text-align:center;text-transform:uppercase}
.hero-cta{left:317px;top:251px;width:90px;height:26px;line-height:26px}
.arrow-c{width:22px;height:22px;border:1px solid rgba(255,255,255,.7);border-radius:50%}
.quote-form{left:478px;top:19px;width:144px;height:160px;background:var(--red);padding:11px 11px;box-shadow:0 2px 6px rgba(0,0,0,.3)}
.field{background:#fff;height:18px;margin-bottom:6.5px;font-size:6.5px;color:#999;padding:5px 8px}
.field.msg{height:37px}
.submit{background:var(--gold);color:#fff;height:22px;line-height:22px;text-align:center;font-size:7.5px;font-weight:700}
.video{left:56px;top:381px;width:234px;height:169px;background:#000}
.video-img{left:56px;top:381px;width:234px;height:156px;background:radial-gradient(circle at 50% 70%,#fbed22,#f78f20 30%,#c8220f 60%,#1a0500)}
.play{left:155px;top:447px;width:36px;height:36px;border-radius:50%;background:var(--red)}
.vbar{left:56px;top:537px;width:234px;height:13px;color:#fff;font-size:4px;line-height:13px}
.who-title{font-size:14px;font-weight:400;color:#222}
.para{font-size:6px;line-height:14px;color:#666}
.sec-title{font-size:14px;color:#222}
.sec-sub{font-size:7.5px;color:#555}
.pager{width:14px;height:14px;border:1px solid #ccc;font-size:8px;line-height:12px;text-align:center;color:#888}
.card-img{top:633px;width:133px;height:103px}
.card-title{top:748px;font-size:8.5px;color:#222}
.card-desc{top:763px;font-size:6.5px;color:#666}
.card-line{top:780px;width:122px;height:1px;background:var(--line)}
.price{top:788px;font-size:7.5px;color:var(--red)}
.stars{top:789px;font-size:6px;color:var(--amber);letter-spacing:.5px}
.blog-band{left:0;top:830px;width:678px;height:173px;background:var(--band)}
.date{top:888px;width:32px;height:34px;background:var(--orange);color:#fff;text-align:center}
.date b{display:block;font-size:12px;font-weight:400;line-height:18px;margin-top:3px}
.date span{display:block;font-size:5.5px;line-height:9px}
.post-title{top:888px;font-size:7.5px;line-height:12px;color:#222;width:110px}
.post-by{top:914px;font-size:5.5px;color:#666}
.post-body{top:928px;width:158px;font-size:5.8px;line-height:13px;color:#666}
.foot-title{font-size:11.5px;font-weight:400;color:#222}
.foot-links{font-size:6.5px;line-height:14px;color:#555}
.email-in{left:66px;top:1069px;width:148px;height:20px;border:1px solid #ccc;font-size:5.5px;color:#999;padding:6px 7px}
.social{top:1118px;width:15px;height:15px;border-radius:50%}
.rule{left:0;top:1158px;width:678px;height:1px;background:#e3e3e3}
.copy{left:0;top:1174px;width:678px;text-align:center;font-size:6.5px;color:#666}
</style>
</head>
<body>
<div class="abs topbar">24 HOUR EMERGENCY SERVICE : <span class="phone">1-800-555-0142, 1-555-014-2088</span></div>
<div class="abs header"></div>
<div class="abs nav" style="left:57px">Home</div>
<div class="abs nav" style="left:116px">About Us</div>
<div class="abs nav" style="left:189px">Products &#x2304;</div>
<div class="abs nav" style="left:440px">Services</div>
<div class="abs brand"><span class="brand-dot"></span>Blazewren</div>

<section>
<div class="abs hero" role="img" aria-label="Concrete wall backdrop"></div>
<div class="abs hero-photo" role="img" aria-label="Red fire extinguisher standing against a wall"></div>
<h1 class="abs hero-title">25 YEARS SERVING<br>SOUTHERN CALIFORNIA</h1>
<p class="abs hero-sub">Exceptional Customer Service and a Commitment to Excellence</p>
<div class="abs btn hero-cta">Contact Here!</div>
<div class="abs arrow-c" style="left:18px;top:196px"></div>
<div class="abs arrow-c" style="left:637px;top:196px"></div>
</section>

<div class="abs quote-btn">REQUEST QUOTE &#x2304;</div>
<form class="abs quote-form">
  <div class="field">Name</div>
  <div class="field">Email</div>
  <div class="field">Phone</div>
  <div class="field msg">Message</div>
  <div class="submit">SUBMIT</div>
</form>

<section class="who">
<div class="abs video"></div>
<div class="abs video-img" role="img" aria-label="Company video still with flames"></div>
<svg class="abs play" viewBox="0 0 36 36"><polygon points="14,10 27,18 14,26" fill="#fff"/></svg>
<div class="abs vbar" style="padding-left:6px">&#9646;&#9646; &nbsp;&#9834;<span style="float:right;margin-right:16px">0:00 / 1:30</span></div>
<h2 class="abs who-title" style="left:324px;top:386px">Who we are?</h2>
<p class="abs para" style="left:325px;top:411px;width:290px">Blazewren Fire &amp; Safety is a certified small business and woman owned provider of fire protection services headquartered in Southern California since 1991.</p>
<p class="abs para" style="left:325px;top:450px;width:290px">We are rebuilding the marketing outreach program to go fully digital, mobile and ready to start aggressive digital sales and marketing outreach programs. So, everything we do website, email, direct mail, phone calls and more must be up to date and using latest technology for SEO, tracking, ROI, sales conversions and more.</p>
<div class="abs btn" style="left:325px;top:520px;width:91px;height:25px;line-height:25px">Read More Info</div>
</section>

<section>
<div class="abs" style="left:55px;top:584px"><span class="sec-title">Our Products</span> &nbsp;<span class="sec-sub">Sales, service and inspection of portable fire extinguishers of any size or requirement.</span></div>
<div class="abs pager" style="left:588px;top:584px">&lsaquo;</div>
<div class="abs pager" style="left:607px;top:584px">&rsaquo;</div>
<div class="abs" style="left:55px;top:614px;width:567px;height:1px;background:var(--line)"></div>

<div class="abs card-img" style="left:56px;background:linear-gradient(#3a8fc4 0 3px,#8c2a1e 3px,#b0442e)" role="img" aria-label="Coiled red fire hose"></div>
<div class="abs card-img" style="left:200px;background:var(--orange)"></div>
<div class="abs" style="left:216px;top:672px;color:#fff;font-size:8.5px;line-height:12px">Kitchen Suppression<br>Systems</div>
<div class="abs" style="left:215px;top:705px;width:66px;height:19px;border:1px solid #fff;color:#fff;font-size:6px;line-height:17px;text-align:center">VIEW DETAILS</div>
<div class="abs card-img" style="left:345px;background:linear-gradient(#a9a9a9,#b4232a 60%,#7a1a18)" role="img" aria-label="Red sprinkler valve wheel"></div>
<div class="abs card-img" style="left:489px;background:linear-gradient(90deg,#3a3a3a,#6d6d6d 50%,#2a2a2a)" role="img" aria-label="Firefighter breathing masks"></div>

<div class="abs card-title" style="left:56px">Portable Fire Extinguishers</div>
<div class="abs card-title" style="left:201px">Kitchen Suppression Systems</div>
<div class="abs card-title" style="left:345px">Building Sprinkler Systems</div>
<div class="abs card-title" style="left:489px">Live Fire Demonstrations</div>
<div class="abs card-desc" style="left:57px">Perform inspection, maintenance...</div>
<div class="abs card-desc" style="left:201px">Perform inspection, maintenance...</div>
<div class="abs card-desc" style="left:346px">Perform inspection, maintenance...</div>
<div class="abs card-desc" style="left:490px">Perform inspection, maintenance...</div>
<div class="abs card-line" style="left:56px"></div><div class="abs card-line" style="left:200px"></div>
<div class="abs card-line" style="left:345px"></div><div class="abs card-line" style="left:489px"></div>
<div class="abs price" style="left:56px">$ 120.00</div><div class="abs stars" style="left:145px">&#9733;&#9733;&#9733;&#9733;&#9733;</div>
<div class="abs price" style="left:200px">$ 120.00</div><div class="abs stars" style="left:289px">&#9733;&#9733;&#9733;&#9733;&#9733;</div>
<div class="abs price" style="left:345px">$ 120.00</div><div class="abs stars" style="left:434px">&#9733;&#9733;&#9733;&#9733;&#9733;</div>
<div class="abs price" style="left:489px">$ 120.00</div><div class="abs stars" style="left:578px">&#9733;&#9733;&#9733;&#9733;&#9733;</div>
</section>

<section>
<div class="abs blog-band"></div>
<div class="abs sec-title" style="left:55px;top:852px">Blog / News</div>
<div class="abs date" style="left:55px"><b>24</b><span>March</span></div>
<div class="abs date" style="left:254px"><b>24</b><span>March</span></div>
<div class="abs date" style="left:453px"><b>24</b><span>March</span></div>
<div class="abs post-title" style="left:95px">FCSA, state &amp; local fire and safety codes.</div>
<div class="abs post-title" style="left:294px">FCSA, state &amp; local fire and safety codes.</div>
<div class="abs post-title" style="left:493px">FCSA, state &amp; local fire and safety codes.</div>
<div class="abs post-by" style="left:95px">By Lena Morrow</div>
<div class="abs post-by" style="left:294px">By Lena Morrow</div>
<div class="abs post-by" style="left:493px">By Lena Morrow</div>
<p class="abs post-body" style="left:55px">Es simplemente el texto de relleno de las imprentas y archivos de texto. Lorem Ipsum ha sido el texto de relleno estándar de las industrias desde el año 1500, cuando un impresor desconocido...</p>
<p class="abs post-body" style="left:254px">Es simplemente el texto de relleno de las imprentas y archivos de texto. Lorem Ipsum ha sido el texto de relleno estándar de las industrias desde el año 1500, cuando un impresor desconocido...</p>
<p class="abs post-body" style="left:453px">Es simplemente el texto de relleno de las imprentas y archivos de texto. Lorem Ipsum ha sido el texto de relleno estándar de las industrias desde el año 1500, cuando un impresor desconocido...</p>
</section>

<footer>
<div class="abs" style="left:66px;top:1030px;font-size:15px;color:#222"><span style="display:inline-block;width:14px;height:14px;border-radius:50%;background:#444;vertical-align:middle;margin-right:4px"></span>Postbird</div>
<div class="abs" style="left:105px;top:1048px;font-size:8px;color:#444">Newsletter</div>
<div class="abs email-in">Enter your email id</div>
<div class="abs btn" style="left:66px;top:1097px;width:65px;height:20px;line-height:20px;font-size:6.5px">Subscribe</div>

<h3 class="abs foot-title" style="left:250px;top:1033px">Welcome</h3>
<div class="abs foot-links" style="left:250px;top:1052px">Home<br>About Us<br>Products<br>Services<br>Blog<br>Contact us</div>

<h3 class="abs foot-title" style="left:346px;top:1033px">Contact Us</h3>
<div class="abs foot-links" style="left:346px;top:1052px">PO Box 410230, 1820 Harbor Crest Way<br>San Diego, CA 92121</div>
<div class="abs foot-links" style="left:346px;top:1082px"><span style="color:var(--orange)">&#9993;</span> hello@blazewrensafety.example</div>
<div class="abs foot-links" style="left:346px;top:1097px"><span style="color:var(--orange)">&#9679;</span> www.blazewrensafety.example</div>
<div class="abs social" style="left:348px;background:#3b5a9a"></div>
<div class="abs social" style="left:366px;background:#1c7bb5"></div>
<div class="abs social" style="left:384px;background:var(--amber)"></div>
<div class="abs social" style="left:402px;background:#3aa9e0"></div>
<div class="abs social" style="left:420px;background:var(--red)"></div>

<div class="abs" style="left:526px;top:1026px;width:66px;height:54px;border-radius:50%;background:radial-gradient(#f0d060,#b08a1c)"></div>
<div class="abs" style="left:538px;top:1095px;width:44px;height:44px;background:#111"></div>

<div class="abs rule"></div>
<div class="abs copy">&copy; 2016. Blazewren Fire and Safety Inc. All rights reserved.</div>
</footer>
</body>
</html>
```